Simple and Clean business card design

We would like the design to be simple clean and to incorporate our colors.

We are open to your design and talent, we have the dots in our logo as we think of it as data points and we connect data points for people.

We are open to see the great creative and clean design you bring to the table

Contact Information for Business Card

please include: name, position, email, phone and website

Font styles to use
Sans Serif

Requirements
Must have
• my colors incorporated, simplicity
Nice to have
• lots of white space, simplicity
Should not have
• complexicity/ complex art

```html
<!DOCTYPE html>
<html lang="en">
<head>
<meta charset="UTF-8">
<title>Bramble Business Card</title>
<link rel="stylesheet" href="https://fonts.googleapis.com/css2?family=Nunito:wght@400;800&display=swap">
<style>
  :root {
    --backdrop-top: #ffffff;
    --backdrop-bottom: #8a8a8a;
    --card: #ffffff;
    --band-blue: #3d70b0;
    --ink: #111111;
    --white: #ffffff;
    --dot-green: #34a853;
    --net-blue: #c3d0e8;
    --net-yellow: #fbe6a4;
    --net-green: #bfe3c8;
    --net-pink: #f6c2bd;
  }
  * { margin: 0; padding: 0; box-sizing: border-box; }
  html, body { width: 1200px; height: 1000px; overflow: hidden; }
  body {
    position: relative;
    background: linear-gradient(180deg, var(--backdrop-top) 0%, #f3f3f3 25%, var(--backdrop-bottom) 100%);
    font-family: "Nunito", sans-serif;
  }
  .card {
    position: absolute;
    background: var(--card);
    overflow: hidden;
    box-shadow: 0 1px 6px rgba(0,0,0,0.18);
  }
  .card--front { left: 258px; top: 41px; width: 684px; height: 443px; }
  .card--back  { left: 258px; top: 520px; width: 676px; height: 437px; }

  .network {
    position: absolute;
    left: 0;
    width: 100%;
    background:
      radial-gradient(circle at 15% 40%, rgba(195,208,232,0.45), transparent 30%),
      radial-gradient(circle at 52% 55%, rgba(251,230,164,0.45), transparent 28%),
      radial-gradient(circle at 82% 35%, rgba(246,194,189,0.40), transparent 26%),
      radial-gradient(circle at 70% 70%, rgba(191,227,200,0.40), transparent 28%),
      linear-gradient(180deg, #fafbfd, #f4f6fa);
  }
  .card--front .network { top: 90px; height: 262px; }
  .card--back .network { top: 0; height: 215px; }

  .wordmark {
    position: absolute;
    left: 0;
    width: 100%;
    display: flex;
    justify-content: center;
    align-items: center;
    gap: 14px;
    color: var(--ink);
    font-weight: 400;
    line-height: 1;
  }
  .wordmark__dot { border-radius: 50%; background: var(--dot-green); flex: none; }
  .card--front .wordmark { top: 62px; font-size: 88px; }
  .card--front .wordmark__dot { width: 28px; height: 28px; }
  .card--back .wordmark { top: 228px; font-size: 62px; }
  .card--back .wordmark__dot { width: 22px; height: 22px; }

  .band {
    position: absolute;
    left: 0;
    bottom: 0;
    width: 100%;
    background: var(--band-blue);
    border-radius: 60px 60px 0 0;
    color: var(--white);
    font-weight: 800;
    font-size: 21px;
  }
  .card--front .band { height: 92px; }
  .card--back .band { height: 59px; border-radius: 58px 58px 0 0; }

  .band__identity {
    position: absolute;
    left: 74px;
    top: 14px;
    width: 160px;
    text-align: center;
    line-height: 34px;
  }
  .band__contact {
    position: absolute;
    left: 338px;
    top: 12px;
    line-height: 35px;
  }
  .band__web {
    width: 100%;
    text-align: center;
    line-height: 59px;
    font-size: 20px;
  }
</style>
</head>
<body>
  <section class="card card--front">
    <div class="network" role="img" aria-label="Faint network of pastel data-point dots joined by thin grey lines"></div>
    <div class="wordmark"><span class="wordmark__dot"></span><span>Bramble</span></div>
    <div class="band">
      <div class="band__identity">
        <p>yourname</p>
        <p>position</p>
      </div>
      <div class="band__contact">
        <p>+ (xx) 555 555 55</p>
        <p>yourmailaddress@mailbox.com</p>
      </div>
    </div>
  </section>

  <section class="card card--back">
    <div class="network" role="img" aria-label="Faint network of pastel data-point dots joined by thin grey lines"></div>
    <div class="wordmark"><span class="wordmark__dot"></span><span>Bramble</span></div>
    <div class="band">
      <p class="band__web">www.bramble-data.com</p>
    </div>
  </section>
</body>
</html>
```